Crimson Ledger.com is wanting to create a Facebook Ad to attract buyers to come to their website. We are wanting buyers to register for free and create an account on Crimson Ledger. com. We want to increase the number of buyers by posting an ad on Facebook groups. The buyer will click the link to our websites registration page.
https://www.crimsonledger.com/account/users/register

Semi Trucks
Semi Trailers
Construction Equipment
Farm Equipment
Trailers
ATV/UTV
Boats
RVs

```html
<!DOCTYPE html>
<html lang="en">
<head>
<meta charset="utf-8">
<title>Crimson Ledger – Register for an account</title>
<link rel="stylesheet" href="https://fonts.googleapis.com/css2?family=Oswald:wght@500;600;700&display=swap">
<style>
  :root {
    --ink: #000000;
    --paper: #ffffff;
    --accent: #e2661f;
    --truck-tone: #8f9a8c;
    --utv-tone: #3e4a3c;
    --loader-tone: #c9a233;
  }
  html, body {
    margin: 0;
    padding: 0;
    width: 1200px;
    height: 1200px;
    overflow: hidden;
    background: var(--ink);
  }
  .ad {
    position: relative;
    width: 1200px;
    height: 1200px;
    background: var(--ink);
    color: var(--paper);
    font-family: "Oswald", "Arial Narrow", sans-serif;
    overflow: hidden;
  }
  .brand {
    position: absolute;
    top: 175px;
    left: 0;
    width: 1200px;
    display: flex;
    justify-content: center;
    align-items: center;
    gap: 26px;
  }
  .brand-mark {
    width: 64px;
    height: 64px;
    background: var(--accent);
  }
  .brand-name {
    font-weight: 700;
    font-size: 100px;
    line-height: 1;
    letter-spacing: 2px;
    text-transform: uppercase;
    color: var(--paper);
    white-space: nowrap;
  }
  .headline {
    position: absolute;
    top: 378px;
    left: 0;
    width: 1200px;
    margin: 0;
    text-align: center;
    font-weight: 600;
    font-size: 47px;
    line-height: 65px;
    text-transform: uppercase;
    white-space: nowrap;
    z-index: 2;
  }
  .gallery {
    position: absolute;
    top: 515px;
    left: 0;
    width: 1200px;
    height: 480px;
  }
  .photo { position: absolute; top: 0; height: 100%; }
  .photo--truck {
    left: 0; width: 420px;
    background: linear-gradient(160deg, #6f8a5a 0%, #d9dcd8 35%, var(--truck-tone) 70%, #9a9a92 100%);
  }
  .photo--utv {
    left: 400px; width: 450px;
    background: linear-gradient(180deg, #8b7a5a 0%, var(--utv-tone) 40%, #2c3338 75%, #6d6a62 100%);
  }
  .photo--loader {
    left: 840px; width: 360px;
    background: linear-gradient(160deg, #6b7f55 0%, var(--loader-tone) 40%, #2a2a26 75%, #7a7a5c 100%);
  }
  .gallery-fade {
    position: absolute;
    inset: 0;
    background:
      linear-gradient(180deg, var(--ink) 0%, rgba(0,0,0,0) 14%, rgba(0,0,0,0) 78%, var(--ink) 100%);
  }
  .categories {
    position: absolute;
    top: 940px;
    left: 0;
    width: 1200px;
    margin: 0;
    text-align: center;
    font-weight: 500;
    font-size: 43px;
    line-height: 56px;
    white-space: nowrap;
    z-index: 2;
  }
  .categories .sep { color: var(--accent); padding: 0 4px; }
  .cta {
    position: absolute;
    top: 1062px;
    left: 137px;
    width: 914px;
    height: 86px;
    background: var(--accent);
    color: var(--paper);
    display: flex;
    align-items: center;
    justify-content: center;
    font-weight: 500;
    font-size: 47px;
    line-height: 1;
    white-space: nowrap;
    text-decoration: none;
  }
</style>
</head>
<body>
<main class="ad">
  <div class="brand">
    <span class="brand-mark" aria-hidden="true"></span>
    <span class="brand-name">Crimson Ledger</span>
  </div>

  <h1 class="headline">Trusted insurance auction site for heavy<br>salvage semi-trucks, trailers, equipment<br>and commercial vehicles</h1>

  <div class="gallery">
    <div class="photo photo--truck" role="img" aria-label="Photo of a white semi truck tractor parked on gravel"></div>
    <div class="photo photo--utv" role="img" aria-label="Photo of a green side-by-side utility vehicle"></div>
    <div class="photo photo--loader" role="img" aria-label="Photo of a yellow compact track loader"></div>
    <div class="gallery-fade" aria-hidden="true"></div>
  </div>

  <p class="categories">
    Semi Trucks <span class="sep">|</span> Semi Trailers <span class="sep">|</span> Construction Equipment<br>
    Farm Equipment <span class="sep">|</span> Trailers <span class="sep">|</span> ATV/UTV <span class="sep">|</span> Boats<span class="sep">|</span> RVs
  </p>

  <a class="cta" href="https://www.crimsonledger.com/account/users/register">Click here to sign in or register for an account</a>
</main>
</body>
</html>
```